Icon-Design für Entwicklung von IT-Anwendungen
Zielgruppe
Entwicklung von IT-Anwendungen - Schwerpunkt sind Intranet-Anwendungen
Aufgabenstellung
Modernes Button-Layout mit Fokus auf 'technisches', eher schnörkelloses Design
1. Gewünscht wird ein modernes Layout für 8 Buttons (vgl. alte Buttons in buttons.png). Für jede Aktion (z.B. Einzelprojekt bearbeiten, Speichern, Löschen, usw.) soll ein aussagefähiges Icon und der jeweilige Text enthalten sein.
2. Für jeden Button soll es eine Highlight-Variante geben (für spätere MouseOver-Anwendung)
3. Weiterhin wird eine Leiste gewünscht, in die die Buttons später integriert werden. Als Farbe soll ein Blauton verwendet werden, der zum restlichen Blau harmoniert.
Technische Vorgaben für Buttons
- Größe jeweils 130 x 34 Pixel
- Hintergrundfarbe transparent
- Photoshop-Dateiformat, so dass Texte editierbar bleiben
Technische Vorgaben für Leiste
- Größe 1320 x 40 Pixel
- PNG-Dateiformat

```html
<!DOCTYPE html>
<html lang="de">
<head>
<meta charset="utf-8">
<title>Button-Leiste Projektverwaltung</title>
<link href="https://fonts.googleapis.com/css2?family=Source+Sans+3:wght@400;700&display=swap" rel="stylesheet">
<style>
  :root{
    --bar-top:#2f6fd1;
    --bar-bottom:#1b52ad;
    --divider:rgba(255,255,255,.28);
    --divider-dark:rgba(0,30,90,.45);
    --label:#ffffff;
    --danger-top:#e42424;
    --danger-bottom:#c4080b;
    --neutral-top:#e1e1e1;
    --neutral-bottom:#b9b9b9;
    --neutral-label:#1f5cc0;
    --heading:#a9a9a9;
    --page:#ffffff;
  }
  html,body{margin:0;padding:0;background:var(--page);overflow:hidden}
  .canvas{position:relative;width:1200px;height:416px;overflow:hidden;font-family:"Source Sans 3",sans-serif}
  .toolbar{
    position:absolute;left:94px;width:1012px;height:26px;
    display:flex;
    background:linear-gradient(var(--bar-top),var(--bar-bottom));
    box-shadow:1px 2px 3px rgba(0,0,0,.35);
  }
  .toolbar--plain{top:67px}
  .toolbar--danger{top:251px;left:96px}
  .toolbar--neutral{top:315px;left:96px}
  .tool-button{
    position:relative;flex:1 1 0;display:flex;align-items:center;
    color:var(--label);font-size:8px;line-height:10px;
    border-left:1px solid var(--divider);
    box-shadow:inset 1px 0 0 var(--divider-dark);
  }
  .tool-button:first-child{border-left:none;box-shadow:none}
  .tool-button__icon{width:26px;height:17px;margin-left:8px;flex:none;fill:currentColor}
  .tool-button__label{margin-left:14px;white-space:nowrap}
  .tool-button--danger-hover{background:linear-gradient(var(--danger-top),var(--danger-bottom))}
  .tool-button--neutral-hover{
    background:linear-gradient(var(--neutral-top),var(--neutral-bottom));
    color:var(--neutral-label);
  }
  .section-title{
    position:absolute;left:95px;top:205px;margin:0;
    font-size:21px;font-weight:700;color:var(--heading);letter-spacing:.2px;
  }
  .pointer{position:absolute;width:24px;height:31px}
  .pointer--danger{left:1087px;top:265px}
  .pointer--neutral{left:326px;top:333px}
</style>
</head>
<body>
<div class="canvas">
<svg width="0" height="0" style="position:absolute">
  <defs>
    <symbol id="i-folder-add" viewBox="0 0 26 17"><path d="M1 3h7l2 2h8v10H3z"/><path d="M4 7h14l-2 9H2z"/><path d="M20 2h2v3h3v2h-3v3h-2V7h-3V5h3z"/></symbol>
    <symbol id="i-doc-search" viewBox="0 0 26 17"><path d="M3 5h7v5l5 7H5l-2-3z"/><circle cx="14" cy="6" r="5" fill="none" stroke="currentColor" stroke-width="2"/><path d="M17 9l4 4-1.5 1.5-4-4z"/></symbol>
    <symbol id="i-folder-search" viewBox="0 0 26 17"><path d="M1 4h6l2 2h6v10H3z"/><path d="M4 8h13l-2 8H2z"/><circle cx="19" cy="6" r="4.5" fill="none" stroke="currentColor" stroke-width="2"/><path d="M22 9l3 3-1.4 1.4-3-3z"/></symbol>
    <symbol id="i-edit" viewBox="0 0 26 17"><path d="M9 2h9l3 4v10H13z"/><path d="M3 9l6-6 3 3-6 6z"/><path d="M2 12l3 1-4 2z"/></symbol>
    <symbol id="i-save-back" viewBox="0 0 26 17"><path d="M2 1h13l3 3v12H2z"/><rect x="5" y="2" width="7" height="5" fill="#2a63c4"/><path d="M17 9a4 4 0 1 1-4 5h2a2 2 0 1 0 2-3v2l-3-3 3-3z" fill="#ffffff" stroke="#2a63c4" stroke-width=".6"/></symbol>
    <symbol id="i-save-next" viewBox="0 0 26 17"><path d="M2 1h13l3 3v12H2z"/><rect x="5" y="2" width="7" height="5" fill="#2a63c4"/><path d="M14 16a4 4 0 0 1 5-6V8l3 3-3 3v-2a2 2 0 0 0-3 4z" fill="#ffffff" stroke="#2a63c4" stroke-width=".6"/></symbol>
    <symbol id="i-duplicate" viewBox="0 0 26 17"><path d="M3 2h7l2 2h10v10H5z"/><path d="M1 5h7l2 2h9v9H2z" stroke="#2a63c4" stroke-width=".8"/><path d="M5 9h17l-3 7H2z" stroke="#2a63c4" stroke-width=".8"/></symbol>
    <symbol id="i-trash" viewBox="0 0 26 17"><path d="M8 2h6v1h5v2H3V3h5z"/><path d="M5 6h12l-1 11H6zM8 8v7h1.3V8zm2.4 0v7h1.3V8zm2.4 0v7h1.3V8z" fill-rule="evenodd"/></symbol>
  </defs>
</svg>

<nav class="toolbar toolbar--plain" aria-label="Projektaktionen">
  <div class="tool-button"><svg class="tool-button__icon"><use href="#i-folder-add"/></svg><span class="tool-button__label" style="margin-left:26px">Neues Projekt<br>anlegen</span></div>
  <div class="tool-button"><svg class="tool-button__icon"><use href="#i-doc-search"/></svg><span class="tool-button__label">Einzelprojektansicht</span></div>
  <div class="tool-button"><svg class="tool-button__icon"><use href="#i-folder-search"/></svg><span class="tool-button__label">Multiprojektansicht</span></div>
  <div class="tool-button"><svg class="tool-button__icon"><use href="#i-edit"/></svg><span class="tool-button__label" style="margin-left:26px">Einzelprojekt<br>bearbeiten</span></div>
  <div class="tool-button"><svg class="tool-button__icon"><use href="#i-save-back"/></svg><span class="tool-button__label" style="margin-left:20px">Speichern und zum<br>letzten Projekt</span></div>
  <div class="tool-button"><svg class="tool-button__icon"><use href="#i-save-next"/></svg><span class="tool-button__label" style="margin-left:20px">Speichern und zum<br>nächsten Projekt</span></div>
  <div class="tool-button"><svg class="tool-button__icon"><use href="#i-duplicate"/></svg><span class="tool-button__label" style="margin-left:20px">Dupliziere<br>dieses Projekt</span></div>
  <div class="tool-button"><svg class="tool-button__icon"><use href="#i-trash"/></svg><span class="tool-button__label">Lösche dieses Projekt</span></div>
</nav>

<h2 class="section-title">Rollover-Effekte:</h2>

<nav class="toolbar toolbar--danger" aria-label="Projektaktionen, Löschen hervorgehoben">
  <div class="tool-button"><svg class="tool-button__icon"><use href="#i-folder-add"/></svg><span class="tool-button__label" style="margin-left:26px">Neues Projekt<br>anlegen</span></div>
  <div class="tool-button"><svg class="tool-button__icon"><use href="#i-doc-search"/></svg><span class="tool-button__label">Einzelprojektansicht</span></div>
  <div class="tool-button"><svg class="tool-button__icon"><use href="#i-folder-search"/></svg><span class="tool-button__label">Multiprojektansicht</span></div>
  <div class="tool-button"><svg class="tool-button__icon"><use href="#i-edit"/></svg><span class="tool-button__label" style="margin-left:26px">Einzelprojekt<br>bearbeiten</span></div>
  <div class="tool-button"><svg class="tool-button__icon"><use href="#i-save-back"/></svg><span class="tool-button__label" style="margin-left:20px">Speichern und zum<br>letzten Projekt</span></div>
  <div class="tool-button"><svg class="tool-button__icon"><use href="#i-save-next"/></svg><span class="tool-button__label" style="margin-left:20px">Speichern und zum<br>nächsten Projekt</span></div>
  <div class="tool-button"><svg class="tool-button__icon"><use href="#i-duplicate"/></svg><span class="tool-button__label" style="margin-left:20px">Dupliziere<br>dieses Projekt</span></div>
  <div class="tool-button tool-button--danger-hover"><svg class="tool-button__icon"><use href="#i-trash"/></svg><span class="tool-button__label">Lösche dieses Projekt</span></div>
</nav>

<nav class="toolbar toolbar--neutral" aria-label="Projektaktionen, Einzelprojektansicht hervorgehoben">
  <div class="tool-button"><svg class="tool-button__icon"><use href="#i-folder-add"/></svg><span class="tool-button__label" style="margin-left:26px">Neues Projekt<br>anlegen</span></div>
  <div class="tool-button tool-button--neutral-hover"><svg class="tool-button__icon"><use href="#i-doc-search"/></svg><span class="tool-button__label">Einzelprojektansicht</span></div>
  <div class="tool-button"><svg class="tool-button__icon"><use href="#i-folder-search"/></svg><span class="tool-button__label">Multiprojektansicht</span></div>
  <div class="tool-button"><svg class="tool-button__icon"><use href="#i-edit"/></svg><span class="tool-button__label" style="margin-left:26px">Einzelprojekt<br>bearbeiten</span></div>
  <div class="tool-button"><svg class="tool-button__icon"><use href="#i-save-back"/></svg><span class="tool-button__label" style="margin-left:20px">Speichern und zum<br>letzten Projekt</span></div>
  <div class="tool-button"><svg class="tool-button__icon"><use href="#i-save-next"/></svg><span class="tool-button__label" style="margin-left:20px">Speichern und zum<br>nächsten Projekt</span></div>
  <div class="tool-button"><svg class="tool-button__icon"><use href="#i-duplicate"/></svg><span class="tool-button__label" style="margin-left:20px">Dupliziere<br>dieses Projekt</span></div>
  <div class="tool-button"><svg class="tool-button__icon"><use href="#i-trash"/></svg><span class="tool-button__label">Lösche dieses Projekt</span></div>
</nav>

<svg class="pointer pointer--danger" viewBox="0 0 24 31" aria-hidden="true"><path d="M1.5 1.5v23l6-6 5 11 4.5-2-5-10.5h9z" fill="#fff" stroke="#000" stroke-width="2.2" stroke-linejoin="round"/></svg>
<svg class="pointer pointer--neutral" viewBox="0 0 24 31" aria-hidden="true"><path d="M1.5 1.5v23l6-6 5 11 4.5-2-5-10.5h9z" fill="#fff" stroke="#000" stroke-width="2.2" stroke-linejoin="round"/></svg>
</div>
</body>
</html>
```